Sports Supplements Company Needs Label Designs

Hello,

We are a sports supplements company named "Veltrane Forge". We produce a line of sports supplements from pre-workouts products to fat burners and multivitamins. Our competitors include companies like Corvalo Provisions and BrawnKettle. Like most companies in the sports supplements field, we need a standard label design for one product that can be later modified a little to be used for the other products. Initially we need a label design for our "BCAA (Branched-Chain Amino Acids)" product. We would like to add other supplements like glutamine and fat burners, so we need a standard design that can be tweaked a bit. The only difference would be the information and ingredients in the other products, which will be provided.

For the design we would like one that reflects a modern, brand-unique approach. It should communicate trust and quality. Competitors designs to be considered as reference would include KDT Fitness, BrawnKettle, and Quenvira. Photos of their products can be seen online in places like liftharbor.example. We would also like to include a couple of small icons to indicate the respective product's main functions. Similar icons can be seen in TWG Provisions products, as an example. Main qualities of the BCAA is "strength", "recovery", "Muscle Growth". The product's name is BCAA Solvexa.

The package will be white, with an undecided lid color (probably black). Color combinations I have in mind are mixed combinations of any of the following colors: red, white, yellow (some light to darker shades), brown, black, green, and blue. But please this does not have to limit your imagination to the design and colors. These are just ideas from top of my head. Since the company's name is Veltrane Forge, I do like the design to represent some sort of "mechanics": I'd like to have some design that includes watch wheels, and maybe a wrench. I also would like the name of the company to be on the label as well, under the logo.

Other project text details and measurements are provided in an attached word document, along with the logo of the company we like to use. We like the format to be Ai.

We'd like a designer to work with in future products, and build a relationship with. As said earlier, we need to hire a designer to work with and modify similar projects with a fixed amount (~$50) for each additional product.

Industry/Entity Type

It Company

Colors
f37122
f78f20
ffc214
fbed22
9bcb3c
ec1f27
0255a3
ffffff
000000

Requirements
Must have
• Some sort of "mechanics": I'd like to have some design that includes watch wheels, and maybe a wrench.
Nice to have
• Some sort of harmonious color mixes. Mixes of yellow or orange with white, or maybe red and black.
Should not have
• Plain label with no designs.
• A simple design.

```html
<!DOCTYPE html>
<html lang="en">
<head>
<meta charset="utf-8">
<title>BCAA Solvexa — Veltrane Forge Label</title>
<link rel="stylesheet" href="https://fonts.googleapis.com/css2?family=Russo+One&family=Roboto+Condensed:wght@400;700&family=Roboto+Mono:wght@700&display=swap">
<style>
  :root {
    --page: #ffffff;
    --label: #f4f5f7;
    --ink: #0d0f12;
    --blue: #1c8fe6;
    --blue-bright: #33b4ff;
    --blue-deep: #0255a3;
    --silver-hi: #f2f3f5;
    --silver-mid: #a9adb3;
    --silver-lo: #5d6167;
    --gear-dark: #c4c8cd;
    --gear-tone: #d9dce0;
    --white: #ffffff;
  }
  * { box-sizing: border-box; margin: 0; padding: 0; }
  html, body { width: 1200px; height: 900px; overflow: hidden; background: var(--page); }
  body { font-family: "Roboto Condensed", sans-serif; color: var(--ink); }

  .label {
    position: absolute; left: 100px; top: 50px; width: 1000px; height: 800px;
    background: var(--label); overflow: hidden;
  }
  .chrome-band {
    position: absolute; left: 0; top: 0; width: 100%; height: 34px;
    background: linear-gradient(180deg, var(--silver-hi) 0%, var(--silver-mid) 45%, var(--silver-lo) 55%, var(--silver-hi) 100%);
  }
  .chrome-band::after {
    content: ""; position: absolute; left: 0; right: 0; bottom: -10px; height: 5px; background: var(--blue);
  }
  .gear-artwork {
    position: absolute; left: 0; top: 44px; width: 100%; height: 660px;
    background:
      radial-gradient(circle at 30% 35%, var(--gear-dark) 0%, rgba(196,200,205,0) 28%),
      radial-gradient(circle at 62% 22%, var(--gear-dark) 0%, rgba(196,200,205,0) 22%),
      radial-gradient(circle at 78% 60%, var(--gear-dark) 0%, rgba(196,200,205,0) 26%),
      radial-gradient(circle at 22% 78%, var(--gear-tone) 0%, rgba(217,220,224,0) 24%),
      radial-gradient(ellipse at 50% 45%, var(--gear-tone) 0%, #e8eaed 45%, var(--label) 80%);
  }

  .brand-tag {
    position: absolute; left: 60px; top: 0; width: 150px; height: 180px;
    background: var(--ink); border: 4px solid var(--blue);
    display: flex; flex-direction: column; align-items: center; justify-content: center; gap: 14px;
  }
  .brand-tag .mark { width: 34px; height: 34px; border: 3px solid var(--white); }
  .brand-tag .name {
    color: var(--white); font-weight: 700; font-size: 20px; line-height: 1.1;
    text-align: center; text-transform: uppercase;
  }

  .product-name {
    position: absolute; left: 0; width: 100%; text-align: center;
    font-family: "Russo One", sans-serif; color: var(--ink);
    -webkit-text-stroke: 5px var(--blue); paint-order: stroke fill;
    line-height: 1;
  }
  .product-name.top { top: 205px; font-size: 160px; letter-spacing: 2px; }
  .product-name.bottom { top: 360px; font-size: 150px; letter-spacing: 1px; }

  .strength-banner {
    position: absolute; left: 160px; top: 530px; width: 680px; height: 48px;
    background: var(--ink); border-bottom: 3px solid var(--blue);
    clip-path: polygon(3% 0, 97% 0, 100% 100%, 0 100%);
    display: flex; align-items: center; justify-content: center;
    font-family: "Roboto Mono", monospace; font-weight: 700; font-size: 30px;
    letter-spacing: 14px; color: var(--white);
  }

  .benefits { position: absolute; left: 0; top: 596px; width: 100%; height: 110px; }
  .benefit-bar {
    position: absolute; left: 140px; top: 84px; width: 720px; height: 22px; border-radius: 11px;
    background: linear-gradient(90deg, var(--blue-deep), var(--blue-bright), var(--blue-deep));
  }
  .benefit { position: absolute; top: 0; width: 180px; text-align: center; }
  .benefit svg { display: block; margin: 0 auto; }
  .benefit .caption {
    position: relative; margin-top: 4px; height: 22px; line-height: 22px;
    font-weight: 700; font-size: 15px; white-space: nowrap;
    color: var(--white); text-transform: uppercase; letter-spacing: 0.5px;
  }
  .benefit.growth { left: 180px; }
  .benefit.recovery { left: 410px; }
  .benefit.power { left: 640px; }

  .claims {
    position: absolute; left: 0; top: 712px; width: 100%;
    display: flex; justify-content: center; gap: 26px;
    font-size: 19px; line-height: 24px; text-transform: uppercase; color: var(--ink);
  }
  .claims li { list-style: none; display: flex; align-items: center; gap: 6px; }
  .claims .tick { width: 17px; height: 17px; background: var(--blue-deep); display: inline-flex; align-items: center; justify-content: center; }

  .count-tab {
    position: absolute; left: 350px; top: 744px; width: 300px; height: 56px;
    background: var(--ink); border-radius: 24px 24px 0 0; padding-top: 6px;
    text-align: center; font-family: "Roboto Mono", monospace; font-weight: 700;
  }
  .count-tab .count { color: var(--white); font-size: 20px; line-height: 24px; letter-spacing: 2px; }
  .count-tab .kind { color: var(--blue-bright); font-size: 14px; line-height: 18px; letter-spacing: 2px; }
  .base-rule { position: absolute; left: 0; bottom: 0; width: 100%; height: 6px; background: var(--blue); }
</style>
</head>
<body>
  <main class="label">
    <div class="chrome-band"></div>
    <div class="gear-artwork" role="img" aria-label="Silver mechanical artwork of interlocking watch gears and a wrench behind the product name"></div>

    <div class="brand-tag">
      <span class="mark"></span>
      <span class="name">Veltrane<br>Forge</span>
    </div>

    <h1 class="product-name top">BCAA</h1>
    <div class="product-name bottom">SOLVEXA</div>

    <div class="strength-banner">ULTRA STRENGTH</div>

    <section class="benefits">
      <div class="benefit-bar"></div>
      <div class="benefit growth">
        <svg width="80" height="80" viewBox="0 0 80 80" aria-hidden="true">
          <circle cx="40" cy="40" r="32" fill="none" stroke="#0d0f12" stroke-width="12" stroke-dasharray="10 6.75"/>
          <circle cx="40" cy="40" r="30" fill="#0d0f12"/>
          <path d="M40 22 L54 38 H45 V56 H35 V38 H26 Z" fill="#ffffff"/>
        </svg>
        <div class="caption">Muscle Growth</div>
      </div>
      <div class="benefit recovery">
        <svg width="80" height="80" viewBox="0 0 80 80" aria-hidden="true">
          <circle cx="40" cy="40" r="32" fill="none" stroke="#0d0f12" stroke-width="12" stroke-dasharray="10 6.75"/>
          <circle cx="40" cy="40" r="30" fill="#0d0f12"/>
          <path d="M54 40 A14 14 0 1 1 48 28" fill="none" stroke="#ffffff" stroke-width="5"/>
          <path d="M44 21 L55 25 L49 35 Z" fill="#ffffff"/>
          <path d="M42 31 L35 42 H41 L38 50 L46 38 H40 Z" fill="#ffffff"/>
        </svg>
        <div class="caption">Recovery</div>
      </div>
      <div class="benefit power">
        <svg width="80" height="80" viewBox="0 0 80 80" aria-hidden="true">
          <circle cx="40" cy="40" r="32" fill="none" stroke="#0d0f12" stroke-width="12" stroke-dasharray="10 6.75"/>
          <circle cx="40" cy="40" r="30" fill="#0d0f12"/>
          <rect x="21" y="27" width="8" height="26" rx="2" fill="#ffffff"/>
          <rect x="51" y="27" width="8" height="26" rx="2" fill="#ffffff"/>
          <rect x="29" y="37" width="22" height="6" fill="#ffffff"/>
        </svg>
        <div class="caption">Strength</div>
      </div>
    </section>

    <ul class="claims">
      <li><span class="tick"><svg width="12" height="12" viewBox="0 0 12 12"><path d="M1.5 6.5 L4.5 9.5 L10.5 2.5" fill="none" stroke="#fff" stroke-width="2"/></svg></span>Stimulates Protein Synthesis</li>
      <li><span class="tick"><svg width="12" height="12" viewBox="0 0 12 12"><path d="M1.5 6.5 L4.5 9.5 L10.5 2.5" fill="none" stroke="#fff" stroke-width="2"/></svg></span>Reduces Muscle Breakdown</li>
      <li><span class="tick"><svg width="12" height="12" viewBox="0 0 12 12"><path d="M1.5 6.5 L4.5 9.5 L10.5 2.5" fill="none" stroke="#fff" stroke-width="2"/></svg></span>Supports Muscle Recovery</li>
    </ul>

    <div class="base-rule"></div>
    <div class="count-tab">
      <div class="count">120 TABLETS</div>
      <div class="kind">DIETARY SUPPLEMENT</div>
    </div>
  </main>
</body>
</html>
```